FLYER: Human Factors in Traffic Crashes - Analysis of Drivers' Responses - training

We are hosting a class in Australia 30, November to 4, December 2020. I would like to have a flyer designed to "sell" the class with description of course topics. I have uploaded a flyer I started on my own but I want it to be professional. Dr. Pelloway only gets to AU every 3-5 years to teach from the US. I would like to have some type of roadway scenery, prefer a nighttime scene.

Target Market(s)

Accident reconstructionists and engineers, police reconstructionists.

Font styles to use
Serif

Colors
fec214

Requirements
Must have
• Name of course and course topics, location of course, price, website and contact information.
Nice to have
• Some type of roadway background, possibly a nighttime scene on a roadway.

```html
<!DOCTYPE html>
<html lang="en">
<head>
<meta charset="utf-8">
<title>Human Factors in Traffic Crashes – Open Class, Manley NSW</title>
<link rel="stylesheet" href="https://fonts.googleapis.com/css2?family=Questrial&family=Montserrat:wght@600;700&display=swap">
<style>
  :root {
    --page-bg: #232323;
    --flyer-bg: #0b0c0e;
    --ink: #ffffff;
    --ink-soft: #e6e6e6;
    --accent: #fec214;
    --road-mid: #3a3b2a;
    --road-glow: #7f7a3a;
    --rule: #8a8a8a;
  }
  * { margin: 0; padding: 0; box-sizing: border-box; }
  html, body {
    width: 1200px; height: 2700px; overflow: hidden;
    background: var(--page-bg);
  }
  .flyer {
    position: absolute; left: 0; top: 0;
    width: 1200px; height: 1697px;
    background: var(--flyer-bg);
    color: var(--ink);
    font-family: "Questrial", "Century Gothic", sans-serif;
    overflow: hidden;
  }
  .road-scene {
    position: absolute; inset: 0;
    background:
      radial-gradient(ellipse 700px 520px at 1000px 1150px, rgba(127,122,58,0.75), transparent 70%),
      radial-gradient(ellipse 520px 380px at 720px 1080px, rgba(150,130,40,0.45), transparent 70%),
      radial-gradient(ellipse 900px 500px at 1100px 1500px, rgba(70,80,70,0.7), transparent 75%),
      linear-gradient(180deg, #08090b 0%, #0c0d10 40%, #15160f 65%, #101210 100%);
  }
  .abs { position: absolute; }
  .title {
    top: 56px; left: 0; width: 1200px;
    text-align: center;
    font-size: 44px; line-height: 51px;
    letter-spacing: 0.5px;
  }
  .title strong { font-family: "Montserrat", sans-serif; font-weight: 700; }
  .presenter {
    top: 258px; left: 0; width: 1200px; text-align: center;
    font-size: 25px; line-height: 30px; color: var(--ink-soft);
  }
  .presenter strong { font-family: "Montserrat", sans-serif; font-weight: 700; color: var(--ink); }
  .tagline {
    top: 356px; left: 0; width: 1200px; text-align: center;
    font-family: "Montserrat", sans-serif; font-weight: 700;
    font-size: 27px; line-height: 35px;
  }
  .topics-heading {
    top: 496px; left: 62px;
    font-family: "Montserrat", sans-serif; font-weight: 700;
    font-size: 46px; letter-spacing: 0.5px;
  }
  .topic-list {
    top: 580px; left: 62px; width: 600px;
    list-style: none;
    font-size: 22.5px; line-height: 26px;
  }
  .topic-list li {
    padding-left: 13px; text-indent: -13px; margin-bottom: 26px;
  }
  .topic-list li::before { content: "• "; font-size: 16px; }
  .fee-box {
    top: 506px; left: 838px; width: 237px; height: 245px;
    border: 2px solid var(--ink);
    text-align: center;
  }
  .fee-label {
    margin-top: 22px;
    font-family: "Montserrat", sans-serif; font-weight: 700;
    font-size: 36px; line-height: 38px;
  }
  .fee-word {
    font-family: "Montserrat", sans-serif; font-weight: 700;
    font-size: 80px; line-height: 80px; letter-spacing: 1px;
  }
  .fee-price { font-size: 28px; line-height: 38px; margin-top: 4px; }
  .rule {
    top: 1416px; left: 69px; width: 1061px; height: 1px;
    background: var(--rule);
  }
  .info { left: 62px; font-size: 24px; }
  .info strong { font-family: "Montserrat", sans-serif; font-weight: 700; }
  .location { top: 1470px; }
  .register { top: 1530px; }
  .contact { top: 1566px; }
  .visit { top: 1612px; font-size: 18.5px; color: var(--ink-soft); }
  .brand {
    top: 1528px; left: 881px; width: 249px; height: 99px;
    display: flex; align-items: center; justify-content: center; gap: 12px;
  }
  .brand-mark { width: 22px; height: 22px; background: var(--accent); }
  .brand-name {
    font-family: "Montserrat", sans-serif; font-weight: 700;
    font-size: 22px; line-height: 26px; color: var(--ink);
  }
</style>
</head>
<body>
  <main class="flyer">
    <div class="road-scene" role="img" aria-label="Nighttime photograph of an empty road with street lamps and painted lane markings lit in yellow"></div>

    <h1 class="abs title">HUMAN FACTORS IN TRAFFIC CRASHES,<br>ANALYSIS OF DRIVERS’ RESPONSES-<br>OPEN CLASS: <strong>MANLEY NSW</strong></h1>

    <p class="abs presenter">Presented by: <strong>Graham Pelloway Ph.D.</strong><br>World renowned Human Factors expert</p>

    <p class="abs tagline">It has been 3 years since Dr. Pelloway has come to AU to teach,<br>don’t miss out on this year’s class.</p>

    <h2 class="abs topics-heading">COURSE TOPICS</h2>
    <ul class="abs topic-list">
      <li>Perception-Response Time</li>
      <li>Response to slow moving or stopped vehicles on multilane high speed roads</li>
      <li>Nighttime recognition</li>
      <li>Headlight mapping demonstration and instruction</li>
      <li>Driver decision making</li>
      <li>Research in IDRR</li>
      <li>Gap acceptance for left turns, right turns, and through movements for drivers, riders, and pedestrians</li>
      <li>Pedestrian walking speeds</li>
      <li>Acceleration</li>
      <li>Lateral acceleration (swerving) for cars, motorcycles, and commercial vehicles</li>
      <li>Forward and backward acceleration of cars, motorcycles and commercial vehicles</li>
      <li>Drivers’ responses to green and yellow traffic signals, deceleration choice, reaction time and probability of stopping</li>
    </ul>

    <div class="abs fee-box">
      <div class="fee-label">COURSE</div>
      <div class="fee-word">FEE</div>
      <div class="fee-price">$1,200 USD<br>$1,730 AU</div>
    </div>

    <div class="abs rule"></div>

    <p class="abs info location"><strong>Location:</strong> Headland Lodge – Sydney Harbor National Park 7 Lookout Point Drive, Manley NSW</p>
    <p class="abs info register"><strong>Register on our website:</strong> www.roadlinesafetygroup.com</p>
    <p class="abs info contact"><strong>or Contact:</strong> dana@roadlinesafetygroup.com &nbsp;|&nbsp; <strong>555-014-2290</strong></p>
    <p class="abs info visit">Visit www.RoadlineResearch.com/about/ &nbsp;to learn more about Dr. Pelloway</p>

    <div class="abs brand">
      <span class="brand-mark"></span>
      <span class="brand-name">ROADLINE<br>SAFETY GROUP</span>
    </div>
  </main>
</body>
</html>
```